Local water manufacturing needs a re-design to an existing label design.

We need to change an existing label design for an established water manufacturing company located in the Bahamas. We are expanding into a new 1.5L size product and would like to do so with an updated label design that incorporates an animated pink conch shell (sample included) with at least one other bright color to match the existing blue background and the pink conch shell. The final design should convey an island feel and vibe. The existing label is only a suggestion. The entire label can be completely changed.

Target Market(s)

Hotels, tourist

Industry/Entity Type

Water Manufacturing

Requirements
Must have
• Bright color that matches blue cap and pink conch shell
Nice to have
• Simple design with sleek modern look.

```html
<!DOCTYPE html>
<html lang="en">
<head>
<meta charset="utf-8">
<title>Coralis Purified Water – 1.5 L Label</title>
<link rel="stylesheet" href="https://fonts.googleapis.com/css2?family=Playfair+Display:wght@600&family=Lexend:wght@600&family=Montserrat:wght@400;500&display=swap">
<style>
  :root {
    --page: #f4f4f4;
    --sunrise: #f39a30;
    --coral: #ee7a62;
    --flamingo: #e55a85;
    --dusk: #9a8aa0;
    --lagoon: #1aa4ba;
    --deep-lagoon: #0e9cb2;
    --white: #ffffff;
    --art-top: #3aa3b8;
    --art-mid: #d9648c;
    --art-bottom: #f0964a;
    --wave-tint: rgba(255, 255, 255, 0.16);
  }
  * { margin: 0; padding: 0; box-sizing: border-box; }
  html, body {
    width: 900px;
    height: 1200px;
    overflow: hidden;
    background: var(--page);
  }
  .label {
    position: absolute;
    left: 198px;
    top: 30px;
    width: 504px;
    height: 1140px;
    background: linear-gradient(180deg,
      var(--sunrise) 0%,
      var(--coral) 20%,
      var(--flamingo) 38%,
      var(--dusk) 58%,
      var(--lagoon) 80%,
      var(--deep-lagoon) 100%);
    color: var(--white);
    text-align: center;
  }
  .brand-name {
    position: absolute;
    top: 44px;
    left: 0;
    width: 100%;
    font-family: "Playfair Display", serif;
    font-weight: 600;
    font-size: 92px;
    line-height: 1;
    color: var(--white);
  }
  .shell-art {
    position: absolute;
    left: 50%;
    top: 180px;
    width: 420px;
    height: 360px;
    transform: translateX(-50%);
    background: linear-gradient(180deg, var(--art-top) 0%, var(--art-mid) 60%, var(--art-bottom) 100%);
    opacity: 0.85;
  }
  .product-name {
    position: absolute;
    top: 590px;
    left: 0;
    width: 100%;
    font-family: "Lexend", sans-serif;
    font-weight: 600;
    font-size: 60px;
    line-height: 1.25;
    letter-spacing: 2px;
    text-transform: uppercase;
  }
  .wave-art {
    position: absolute;
    left: 20px;
    top: 770px;
    width: 464px;
    height: 80px;
    background: var(--wave-tint);
  }
  .tagline {
    position: absolute;
    top: 880px;
    left: 0;
    width: 100%;
    font-family: "Montserrat", sans-serif;
    font-weight: 500;
    font-size: 30px;
    letter-spacing: 1px;
  }
  .description {
    position: absolute;
    top: 930px;
    left: 0;
    width: 100%;
    font-family: "Montserrat", sans-serif;
    font-weight: 400;
    font-size: 21px;
    line-height: 1.35;
  }
  .volume {
    position: absolute;
    top: 1060px;
    left: 0;
    width: 100%;
    font-family: "Montserrat", sans-serif;
    font-weight: 400;
    font-size: 22px;
  }
</style>
</head>
<body>
  <main class="label">
    <h1 class="brand-name">Coralis</h1>
    <div class="shell-art" role="img" aria-label="Illustration of a pink and teal conch shell"></div>
    <h2 class="product-name">Purified<br>Water</h2>
    <div class="wave-art" role="img" aria-label="Decorative flowing wave lines"></div>
    <p class="tagline">MINERALS ADDED</p>
    <p class="description">Enhanced with essential minerals<br>for a crisp, refreshing taste</p>
    <p class="volume">1.5 Liter</p>
  </main>
</body>
</html>
```